A3 Internet Cafe advertising posters required - Targetting South Asian & Filipino customers

An internet cafe based within a male-only labour accomodation facility in the United Arab Emirates needs to advertise its presence and services to the employees who live at the facility.

The cafe is called "The Byte Nook" and it offers customers the opportunity to use high-speed broadband internet to engage in activities such as Vocali Web Cam chat with family back home, email, pagemesh, etc, as well as movies and other entertainment from a variety of countries including India. Customers can also purchase refreshments such as biscuits, cakes, tea, 'chai karak' (a local kind of tea), cold soft drinks.

The cost of the internet at the cafe is 5 AED per hour, however users can purchase 10 hours for 40 AED - which should be promoted as a special offer, and these 10 hours can be used whenever the user wishes with no validity limits.

The poster should seek to inform and promote the cafe, the opening hours of the cafe are 11AM - 12AM (MIDNIGHT) every day.

Target Market(s)

male, semi skilled labourers, mostly indian, pakistani with significant filipino proportion

Industry/Entity Type

Entertainment

Requirements
Must have
• photo - centric, the customers are mostly semi-skilled labourers with limited grasp of english, photos that communicate the concepts of watching movies, having tea, speaking to family back home via a computer would work best.
Should not have
• anything sexually suggestive

```html
<!DOCTYPE html>
<html lang="en">
<head>
<meta charset="utf-8">
<title>The Byte Nook Internet Cafe</title>
<link rel="stylesheet" href="https://fonts.googleapis.com/css2?family=Ubuntu:wght@300;500;700&family=Kreon:wght@700&display=swap">
<style>
  :root {
    --sky-top: #8fd9d6;
    --sky-mid: #7cc5c3;
    --sky-low: #6aaaa9;
    --wall-maroon: #7d4650;
    --wall-dark: #6a3540;
    --panel-yellow: rgba(232, 242, 38, 0.93);
    --band-yellow: #cdd31b;
    --ink: #111111;
    --accent-orange: #f26a1b;
    --accent-blue: #1467d8;
    --white: #ffffff;
  }
  * { margin: 0; padding: 0; box-sizing: border-box; }
  html, body { width: 848px; height: 1200px; overflow: hidden; }
  body {
    position: relative;
    background: linear-gradient(180deg,
      var(--sky-top) 0%,
      var(--sky-mid) 40%,
      var(--sky-low) 58%,
      var(--wall-maroon) 64%,
      var(--wall-dark) 79%,
      var(--band-yellow) 80%);
    font-family: "Kreon", Georgia, serif;
    color: var(--ink);
  }
  .backdrop {
    position: absolute; left: 0; top: 600px; width: 848px; height: 360px;
    background: radial-gradient(ellipse at 30% 20%, rgba(220,215,60,0.55), transparent 55%),
                radial-gradient(ellipse at 75% 10%, rgba(220,215,60,0.45), transparent 50%);
  }
  .brand {
    position: absolute; left: 0; top: 36px; width: 848px; text-align: center;
    font-family: "Ubuntu", Arial, sans-serif; color: var(--white);
  }
  .brand-dot {
    display: block; width: 108px; height: 108px; margin: 0 auto 20px;
    border-radius: 50%; background: var(--accent-blue);
  }
  .brand-name { font-weight: 700; font-size: 53px; line-height: 1; }
  .brand-sub { font-weight: 300; font-size: 36px; line-height: 1.1; margin-top: 2px; }
  .divider {
    position: absolute; left: 276px; top: 262px; width: 426px; height: 2px;
    background: linear-gradient(90deg, transparent, var(--white) 30%, var(--white) 70%, transparent);
  }
  .hours {
    position: absolute; left: 0; top: 280px; width: 848px; text-align: center;
    font-family: "Ubuntu", Arial, sans-serif;
  }
  .hours-label { color: var(--accent-blue); font-weight: 500; font-size: 31px; line-height: 1.1; }
  .hours-time { color: var(--white); font-weight: 300; font-size: 34px; line-height: 1.2; }
  .panel { position: absolute; background: var(--panel-yellow); }
  .panel-rate { left: 0; top: 410px; width: 427px; height: 86px;
    display: flex; align-items: center; justify-content: center; font-size: 26px; }
  .panel-offer { left: 454px; top: 376px; width: 394px; height: 174px; text-align: center; padding-top: 22px; }
  .offer-title { color: var(--accent-orange); font-size: 28px; }
  .offer-deal { font-size: 29px; margin-top: 14px; }
  .offer-note { font-size: 16px; line-height: 1.3; }
  .panel-services { left: 0; top: 534px; width: 427px; height: 334px; }
  .services-title { position: absolute; left: 34px; top: 62px; color: var(--accent-orange); font-size: 18px; }
  .services-list { position: absolute; left: 77px; top: 108px; list-style: none; font-size: 24px; line-height: 34px; }
  .panel-shop { left: 454px; top: 600px; width: 394px; height: 335px; }
  .shop-title { position: absolute; left: 101px; top: 48px; color: var(--accent-orange); font-size: 29px; }
  .shop-list { position: absolute; left: 99px; top: 102px; list-style: none; font-size: 25px; line-height: 36px; }
  .gallery { position: absolute; top: 998px; height: 173px; }
  .photo-entrance { left: 17px; width: 231px; background: linear-gradient(180deg, #d9dde0, #b9bcbd); }
  .photo-hall-a { left: 266px; width: 131px; background: linear-gradient(180deg, #bfc3c4, #6d6458 70%, #d8c9b5); }
  .photo-hall-b { left: 413px; width: 128px; background: linear-gradient(180deg, #c9cbcb, #5f574d 70%, #d6c5ae); }
  .photo-counter { left: 557px; width: 129px; background: linear-gradient(180deg, #2b2d2b, #c9c9b6 55%, #e4e0d4); }
  .photo-shopfront { left: 702px; width: 130px; background: linear-gradient(180deg, #e6e9e6, #a8aa8c 60%, #d7d4cf); }
</style>
</head>
<body>
  <div class="backdrop" role="img" aria-label="Soft blurred view of the cafe interior behind the panels"></div>

  <header class="brand">
    <span class="brand-dot"></span>
    <h1 class="brand-name">The Byte Nook</h1>
    <p class="brand-sub">Internet Cafe</p>
  </header>
  <div class="divider"></div>

  <section class="hours">
    <p class="hours-label">OPENS</p>
    <p class="hours-time">11AM - 12AM (MIDNIGHT) daily</p>
  </section>

  <section class="panel panel-rate"><p>5 AED per hour</p></section>

  <section class="panel panel-offer">
    <p class="offer-title">Special offer!</p>
    <p class="offer-deal">10 hours for 40 AED</p>
    <p class="offer-note">-can be used whenever the user<br>&nbsp;&nbsp;wishes with no validity limits.</p>
  </section>

  <section class="panel panel-services">
    <p class="services-title">high-speed broadband internet for</p>
    <ul class="services-list">
      <li>Vocali Web Cam chat</li>
      <li>email</li>
      <li>pagemesh, etc</li>
      <li>as well as movies and</li>
      <li>other entertainment</li>
    </ul>
  </section>

  <section class="panel panel-shop">
    <p class="shop-title">We also Sell</p>
    <ul class="shop-list">
      <li>&nbsp;biscuits</li>
      <li>cakes</li>
      <li>tea</li>
      <li>'chai karak'</li>
      <li>cold soft drinks.</li>
    </ul>
  </section>

  <div class="gallery photo-entrance" role="img" aria-label="Photo of the cafe entrance with glass doors"></div>
  <div class="gallery photo-hall-a" role="img" aria-label="Photo of rows of computer desks and chairs"></div>
  <div class="gallery photo-hall-b" role="img" aria-label="Photo of the computer hall seen down the aisle"></div>
  <div class="gallery photo-counter" role="img" aria-label="Photo of the cafe counter area at night"></div>
  <div class="gallery photo-shopfront" role="img" aria-label="Photo of the snack and drinks counter"></div>
</body>
</html>
```